Creative Brief
Eastmoor Directorate - Bahrain
Business Cards + Stationary materials.
Simple
Tariq Yousef Al-Mansoori
Head of Financial Affairs
P.O. Box 37182, Awali. Kingdom of Bahrain
talmansoori@eastmoor-dir.example
www.eastmoor-dir.example
We would like the design to include the following colors : cyan, golden & silver. But we are open to new ideas that match our new logo.
Stationary items include :
- A4 letterhead ( would prefer the logo in the top middle section so that we can write the office name on either side of the A4 paper. We would like to use the attached watermark image ( you can change the color to match the theme )
- Notepad
- Presentation folder
- Envelopes ( A4, A3, basically the whole nine yards)
a short explanation on the attached files :
* ED Logo : main logo that represents our office (available in B&W and colored)
* Watermark : design we want as a watermark on the stationary
* Horizon : logo (available in different sizes) that should appear close to the address line and should appear on all stationary materials and business cards. This represents Bahrain horizon plan for economic development, more info can be found here : http://www.horizonplan.example/web/ , or http://wiki.example.org/wiki/Bahrain_Horizon_Plan
We would like to also point out that the back side of the business card MUST include the same information as the front but in Arabic language, you can find the translated info below.
Name : طارق يوسف المنصوري
Title : رئيس الموارد المالية
address :
ص.ب 37182، عوالي. مملكة البحرين
all the other info should be the same.
We wouldn't mind seeing different types of fonts as long as they are professional, serious and formal.
ED Logo : main logo that represents our office - in black and white
ED Logo : main logo that represents our office - colored
design we want as a watermark on the stationary
logo that should appear close to the address line and should appear on all stationary materials and business cards. This represents Bahrain horizon plan for economic development, more info can be found here : http://www.horizonplan.example/web/ ,or http://wiki.example.org/wiki/Bahrain_Horizon_Plan

```html
<!DOCTYPE html>
<html lang="en">
<head>
<meta charset="utf-8">
<title>Eastmoor Directorate – Stationery</title>
<link rel="stylesheet" href="https://fonts.googleapis.com/css2?family=Open+Sans:wght@400;600;700&family=Noto+Naskh+Arabic:wght@400;600&display=swap">
<style>
:root{
  --bg:#d9d6d0;
  --paper:#f4f4f2;
  --paper-shade:#e9e9e7;
  --silver:#8c9096;
  --silver-dark:#6f737a;
  --blue:#2a6db0;
  --gold:#d6b779;
  --gold-light:#efdcb1;
  --ink:#5a5e64;
  --line:#c9cbcf;
}
*{margin:0;padding:0;box-sizing:border-box}
html,body{width:1200px;height:862px;overflow:hidden;background:var(--bg)}
body{position:relative;font-family:"Open Sans",Arial,sans-serif;color:var(--ink)}
.item{position:absolute;background:var(--paper);box-shadow:0 2px 6px rgba(0,0,0,.25);overflow:hidden}
.office{font-size:7px;color:var(--blue);font-weight:600;white-space:nowrap}
.office span{color:var(--silver);font-weight:400}
.brand{display:flex;align-items:center;gap:4px;color:var(--blue);font-weight:700;white-space:nowrap;direction:ltr}
.brand i{display:block;border-radius:50%;background:var(--blue);flex:none}
.brand.sm{font-size:6px}.brand.sm i{width:7px;height:7px}
.brand.lg{font-size:22px;gap:10px}.brand.lg i{width:26px;height:26px}
.brand.md{font-size:11px;gap:6px}.brand.md i{width:12px;height:12px}
.tiny{font-size:4.5px;line-height:1.5;color:var(--silver)}
.ar{font-family:"Noto Naskh Arabic",serif;direction:rtl}
.fill-art{background:linear-gradient(180deg,#d9c79c,#b59a63);border-radius:50%}
.watermark{background:rgba(140,144,150,.18);border-radius:6px}
.goldband{background:linear-gradient(90deg,var(--gold-light),var(--gold))}

/* business cards */
.card{left:12px;top:7px;width:132px;height:72px;padding:7px}
.card .brand{position:absolute;right:7px;top:7px}
.card .office{position:absolute;left:7px;top:22px}
.card .who{position:absolute;left:7px;bottom:7px}
.card .name{font-size:6px;color:var(--blue);font-weight:700}
.card-back{left:149px;top:7px;width:132px;height:72px;padding:7px;text-align:right}
.card-back .brand{position:absolute;left:7px;top:7px}
.card-back .office{position:absolute;right:7px;top:22px}
.card-back .who{position:absolute;right:7px;bottom:7px}
.card-back .name{font-size:7px;color:var(--blue);font-weight:600}

/* compliments slip */
.slip{left:12px;top:91px;width:211px;height:101px;padding:10px}
.slip .brand{margin-top:6px}
.slip .foot{position:absolute;left:10px;bottom:8px;right:10px;border-top:1px solid var(--line);padding-top:3px}

/* envelope */
.envelope{left:12px;top:197px;width:211px;height:101px;background:var(--silver)}
.envelope svg{position:absolute;left:0;top:0}
.envelope .brand{position:absolute;left:50%;top:28px;transform:translateX(-50%);color:#fff}
.envelope .brand i{background:#fff}

/* notepad */
.notepad{left:233px;top:91px;width:144px;height:211px;padding:12px 10px;
  background:repeating-linear-gradient(var(--paper) 0 13px,var(--line) 13px 14px) var(--paper);background-origin:content-box}
.notepad .brand{position:absolute;right:8px;top:6px;background:var(--paper);padding:2px}

/* fax */
.fax{left:384px;top:7px;width:202px;height:264px;padding:12px}
.fax .brand{position:absolute;right:10px;top:10px}
.fax .office{margin-top:14px}
.fax h2{font-size:9px;font-weight:600;color:var(--ink);margin:12px 0 8px}
.fax table{width:100%;border-collapse:collapse;font-size:5px}
.fax td{border-bottom:1px solid var(--line);padding:5px 2px}
.fax .opts{display:flex;gap:8px;font-size:4.5px;margin-top:8px}
.fax .base{position:absolute;left:0;right:0;bottom:0;height:16px}

/* letterhead */
.letterhead{left:590px;top:7px;width:298px;height:413px;padding:12px}
.letterhead .brand{position:absolute;right:12px;top:13px}
.letterhead .rule{position:absolute;left:12px;right:12px;top:30px;border-top:1px solid var(--line)}
.letterhead .foot{position:absolute;left:12px;right:12px;bottom:10px;border-top:1px solid var(--line);padding-top:3px;display:flex;justify-content:space-between}

/* back sheet */
.backsheet{left:893px;top:7px;width:298px;height:413px;background:var(--silver)}
.backsheet .watermark{position:absolute;left:79px;top:150px;width:140px;height:60px;background:rgba(255,255,255,.12)}
.backsheet .url{position:absolute;width:100%;top:222px;text-align:center;font-size:7px;color:rgba(255,255,255,.45)}

/* with compliments card */
.wc{left:12px;top:307px;width:240px;height:132px;padding:10px}
.wc .goldband{position:absolute;left:0;right:0;top:0;height:40px}
.wc .office{position:relative}
.wc .title{position:absolute;left:12px;top:52px;font-size:8px;font-weight:600;color:var(--ink)}
.wc .foot{position:absolute;left:10px;right:10px;bottom:10px;display:flex;gap:6px}
.wc .foot div{flex:1;border-top:1px solid var(--line);padding-top:2px}

/* cd */
.cd{left:271px;top:305px;width:132px;height:132px;border-radius:50%;background:var(--paper)}
.cd .hole{position:absolute;left:50%;top:50%;width:30px;height:30px;margin:-15px;border-radius:50%;background:var(--bg);box-shadow:0 0 0 7px #e3e3e3}
.cd .art{position:absolute;left:40px;top:96px;width:52px;height:18px}
.cd .brand{position:absolute;left:50%;top:14px;transform:translateX(-50%)}

/* cd sleeve */
.sleeve{left:427px;top:288px;width:156px;height:144px}
.sleeve .brand{position:absolute;left:12px;top:100px;transform:rotate(-90deg);transform-origin:left top}
.sleeve .art{position:absolute;left:50px;top:60px;width:56px;height:22px}

/* folders */
.folder{top:449px;height:403px}
.folder-back{left:12px;width:283px}
.folder-back .block{position:absolute;left:0;bottom:30px;width:150px;height:100px;display:flex;align-items:center;justify-content:center}
.folder-inner{left:314px;width:283px}
.folder-inner .watermark{position:absolute;left:71px;top:95px;width:140px;height:60px}
.folder-inner .url{position:absolute;width:100%;top:165px;text-align:center;font-size:7px;color:#b9bcc0}
.folder-front{left:624px;width:566px;display:flex}
.folder-front .panel{position:relative;flex:1}
.folder-front .panel+.panel{border-left:1px solid var(--paper-shade)}
.folder-front .center{position:absolute;left:0;right:0;top:130px;display:flex;flex-direction:column;align-items:center;gap:14px}
.folder-front .art{width:190px;height:80px}
.folder-front .pocket{position:absolute;left:0;right:0;bottom:0;height:95px;clip-path:polygon(30% 0,100% 0,100% 100%,0 100%,0 55%)}
.folder-front .pocket .brand{position:absolute;right:20px;bottom:30px}
</style>
</head>
<body>

<div class="item card">
  <div class="brand sm"><i></i>Eastmoor Directorate</div>
  <div class="office">Governor's Office</div>
  <div class="who">
    <div class="name">Tariq Yousef Al-Mansoori</div>
    <div class="tiny">Head of Financial Affairs<br>P.O. Box 37182, Awali. Kingdom of Bahrain<br>talmansoori@eastmoor-dir.example</div>
  </div>
</div>

<div class="item card-back ar">
  <div class="brand sm"><i></i>Eastmoor Directorate</div>
  <div class="office">مكتب المحافظ</div>
  <div class="who">
    <div class="name">طارق يوسف المنصوري</div>
    <div class="tiny">رئيس الموارد المالية<br>ص.ب 37182، عوالي. مملكة البحرين</div>
  </div>
</div>

<div class="item slip">
  <div class="office">Governor's Office <span>| مكتب المحافظ</span></div>
  <div class="brand sm"><i></i>Eastmoor Directorate</div>
  <div class="foot tiny">P.O. Box 37182, Awali. Kingdom of Bahrain · www.eastmoor-dir.example</div>
</div>

<div class="item envelope">
  <svg width="211" height="101" viewBox="0 0 211 101" aria-hidden="true"><path d="M0 0 L105 58 L211 0" fill="none" stroke="#7d8187" stroke-width="1"/></svg>
  <div class="brand sm"><i></i>Eastmoor Directorate</div>
</div>

<div class="item notepad">
  <div class="brand sm"><i></i>Eastmoor Directorate</div>
</div>

<div class="item fax">
  <div class="brand sm"><i></i>Eastmoor Directorate</div>
  <div class="office">Governor's Office <span>| مكتب المحافظ</span></div>
  <h2>Facsimile transmittal</h2>
  <table>
    <tr><td>To</td><td></td><td>Fax</td><td></td></tr>
    <tr><td>From</td><td></td><td>Date</td><td></td></tr>
    <tr><td>Re</td><td></td><td>Pages</td><td></td></tr>
  </table>
  <div class="opts"><span>□ Urgent</span><span>□ For review</span><span>□ Please reply</span><span>□ Please comment</span></div>
  <div class="base goldband"></div>
</div>

<div class="item letterhead">
  <div class="office">Governor's Office <span>| مكتب المحافظ</span></div>
  <div class="brand sm"><i></i>Eastmoor Directorate</div>
  <div class="rule"></div>
  <div class="foot tiny"><span>P.O. Box 37182, Awali. Kingdom of Bahrain</span><span>www.eastmoor-dir.example</span></div>
</div>

<div class="item backsheet">
  <div class="watermark" role="img" aria-label="Faint Arabic calligraphy watermark"></div>
  <div class="url">www.eastmoor-dir.example</div>
</div>

<div class="item wc">
  <div class="goldband"></div>
  <div class="office">Governor's Office <span>| مكتب المحافظ</span></div>
  <div class="title">With Compliments</div>
  <div class="foot tiny"><div>Awali</div><div>www.eastmoor-dir.example</div><div>Kingdom of Bahrain</div></div>
</div>

<div class="item cd">
  <div class="brand sm"><i></i>Eastmoor Directorate</div>
  <div class="hole"></div>
  <div class="art fill-art" role="img" aria-label="Fort illustration"></div>
</div>

<div class="item sleeve">
  <div class="brand sm"><i></i>Eastmoor Directorate</div>
  <div class="art fill-art" role="img" aria-label="Fort illustration"></div>
</div>

<div class="item folder folder-back">
  <div class="block goldband"><div class="brand md"><i></i>Eastmoor Directorate</div></div>
</div>

<div class="item folder folder-inner">
  <div class="watermark" role="img" aria-label="Faint Arabic calligraphy watermark"></div>
  <div class="url">www.eastmoor-dir.example</div>
</div>

<div class="item folder folder-front">
  <div class="panel">
    <div class="center">
      <div class="brand lg"><i></i>Eastmoor Directorate</div>
      <div class="art fill-art" role="img" aria-label="Fort illustration in a gold oval"></div>
    </div>
  </div>
  <div class="panel">
    <div class="pocket goldband"><div class="brand md"><i></i>Eastmoor Directorate</div></div>
  </div>
</div>

</body>
</html>
```